HomeBridle business card and stationary design

We are looking for a simple yet elegant design for our mortgage company business card and stationary.

The card should include:
Name (Derek Walsh)
Title (CEO)
Phone Number (614-208-3917)
Address (48 Birchfield Court, Suite 314, Marlow, OH 43952)
Email (email@homebridle-example.com)
"NMLS" i.e. (NMLS 61947)
"Company NMLS" (Company NMLS 472815)

See above

```html
<!DOCTYPE html>
<html lang="en">
<head>
<meta charset="utf-8">
<title>HomeBridle Business Card</title>
<link href="https://fonts.googleapis.com/css2?family=Montserrat:wght@400;500;600;700&display=swap" rel="stylesheet">
<style>
  :root {
    --page-bg: #5a5a5c;
    --card-white: #ffffff;
    --card-navy: #1b2531;
    --brand-blue: #29a8e0;
    --ink-dark: #1b2531;
    --ink-light: #ffffff;
  }
  * { box-sizing: border-box; margin: 0; padding: 0; }
  html, body {
    width: 1200px;
    height: 900px;
    overflow: hidden;
    background: var(--page-bg);
    font-family: "Montserrat", sans-serif;
  }
  .sheet {
    position: relative;
    width: 1200px;
    height: 900px;
  }
  .card {
    position: absolute;
    left: 260px;
    width: 680px;
    height: 389px;
    overflow: hidden;
    box-shadow: 0 6px 18px rgba(0,0,0,0.35);
  }
  .card--front { top: 45px; background: var(--card-white); }
  .card--back { top: 466px; background: var(--card-navy); color: var(--ink-light); }

  .wordmark {
    font-weight: 600;
    letter-spacing: 1px;
    line-height: 1;
  }
  .card--front .wordmark {
    position: absolute;
    left: 0; right: 0;
    top: 140px;
    text-align: center;
    font-size: 62px;
    color: var(--ink-dark);
  }
  .front-url {
    position: absolute;
    left: 0; right: 0;
    bottom: 36px;
    text-align: center;
    font-size: 15px;
    font-weight: 600;
    letter-spacing: 1.5px;
    color: var(--brand-blue);
  }

  .holder {
    position: absolute;
    left: 44px;
    top: 48px;
  }
  .holder__name {
    font-size: 27px;
    font-weight: 700;
    color: var(--brand-blue);
    letter-spacing: 0.5px;
  }
  .holder__title {
    font-size: 13px;
    font-weight: 500;
    letter-spacing: 1.5px;
    margin-top: 4px;
  }
  .card--back .wordmark {
    position: absolute;
    right: 44px;
    top: 92px;
    font-size: 50px;
    color: var(--ink-light);
  }
  .licences {
    position: absolute;
    left: 44px;
    bottom: 52px;
    font-size: 15px;
    letter-spacing: 1.5px;
    line-height: 1.7;
  }
  .contact {
    position: absolute;
    left: 390px;
    bottom: 40px;
    font-size: 14px;
    letter-spacing: 1.2px;
    line-height: 1.6;
  }
  .contact__address { margin-bottom: 8px; }
  .contact__row {
    display: flex;
    align-items: center;
    gap: 10px;
  }
  .contact__icon { width: 14px; height: 14px; flex: none; }
  .contact__icon path, .contact__icon circle { fill: var(--brand-blue); }
  .accent-band {
    position: absolute;
    left: 0; right: 0; bottom: 0;
    height: 13px;
    background: var(--brand-blue);
  }
</style>
</head>
<body>
<main class="sheet">
  <section class="card card--front">
    <div class="wordmark">HomeBridle</div>
    <div class="front-url">www.homebridle.com</div>
  </section>

  <section class="card card--back">
    <div class="holder">
      <div class="holder__name">Derek Walsh</div>
      <div class="holder__title">CEO</div>
    </div>

    <div class="wordmark">HomeBridle</div>

    <div class="licences">
      <div>NMLS 61947</div>
      <div>Company NMLS 472815</div>
    </div>

    <div class="contact">
      <div class="contact__address">48 Birchfield Court, Suite 314,<br>Marlow, OH 43952</div>
      <div class="contact__row">
        <svg class="contact__icon" viewBox="0 0 24 24" aria-hidden="true"><path d="M6.6 10.8a15.1 15.1 0 0 0 6.6 6.6l2.2-2.2a1 1 0 0 1 1-.25 11.4 11.4 0 0 0 3.6.57 1 1 0 0 1 1 1V20a1 1 0 0 1-1 1A17 17 0 0 1 3 4a1 1 0 0 1 1-1h3.5a1 1 0 0 1 1 1c0 1.25.2 2.45.57 3.6a1 1 0 0 1-.25 1z"/></svg>
        <span>614-208-3917</span>
      </div>
      <div class="contact__row">
        <svg class="contact__icon" viewBox="0 0 24 24" aria-hidden="true"><path d="M2 5h20v2l-10 6L2 7z"/><path d="M2 9l10 6 10-6v10H2z"/></svg>
        <span>email@homebridle-example.com</span>
      </div>
      <div class="contact__row">
        <svg class="contact__icon" viewBox="0 0 24 24" aria-hidden="true"><circle cx="12" cy="12" r="10"/></svg>
        <span>www.homebridle.com</span>
      </div>
    </div>

    <div class="accent-band"></div>
  </section>
</main>
</body>
</html>
```